Stationery Project with Logo Design

We need stationery & logo design for a new small boutique marketing company based in Perth Western Australia. The company is called Blue Harbour Marketing.

We offer marketing services to small-to-medium business.

We would like to see designs strong & innovative designs and should use red as one of the colours.

The final design should communicate innovation and fun.

Target Market(s)

Small to medium business owners between 20 - 50 years

Industry/Entity Type

Business

Logo Text

```html
<!DOCTYPE html>
<html lang="en">
<head>
<meta charset="utf-8">
<title>Blue Harbour Marketing — Stationery</title>
<link href="https://fonts.googleapis.com/css2?family=Oswald:wght@600&display=swap" rel="stylesheet">
<style>
  :root {
    --brand-red: #a51627;
    --paper: #ffffff;
    --backdrop: #b8b8b8;
    --watermark: #e3e3e3;
  }
  * { box-sizing: border-box; margin: 0; padding: 0; }
  html, body { width: 1200px; height: 1000px; overflow: hidden; }
  body {
    position: relative;
    background: var(--backdrop);
    font-family: "Oswald", "Arial Narrow", sans-serif;
  }
  .item { position: absolute; overflow: hidden; }
  .paper { background: var(--paper); }
  .red { background: var(--brand-red); }

  .brand {
    position: absolute;
    font-weight: 600;
    color: var(--brand-red);
    line-height: 1.1;
    text-transform: uppercase;
    letter-spacing: 0.02em;
    white-space: nowrap;
  }
  .brand.on-red { color: var(--paper); text-align: center; }
  .brand.centered { text-align: center; }

  .rule { position: absolute; background: var(--brand-red); }
  .rule.light { background: var(--paper); }
  .divider { position: absolute; width: 4px; background: var(--brand-red); }

  /* folder front */
  .folder-front { left: 41px; top: 55px; width: 363px; height: 306px; }
  .folder-front .brand { left: 18px; top: 108px; font-size: 14px; }
  .folder-front .divider { left: 129px; top: 95px; height: 66px; }
  .folder-front .rule { left: 0; top: 234px; width: 100%; height: 5px; }
  .folder-front .band { position: absolute; left: 0; top: 242px; width: 100%; height: 64px; background: var(--brand-red); }

  /* pencils */
  .pencil { position: absolute; top: 388px; width: 14px; height: 290px; }
  .pencil .tip { display: block; }
  .pencil .body { position: absolute; top: 16px; width: 14px; height: 274px; background: var(--brand-red); }

  /* letterhead */
  .letterhead { left: 505px; top: 0; width: 343px; height: 533px; }
  .letterhead .brand { left: 0; width: 100%; top: 18px; font-size: 14px; }
  .letterhead .watermark {
    position: absolute; left: 0; width: 100%; top: 180px;
    font-weight: 600; font-size: 40px; line-height: 1.05;
    text-transform: uppercase; color: var(--watermark); text-align: center;
  }
  .letterhead .rule { left: 0; top: 473px; width: 100%; height: 5px; }

  /* red folder back */
  .folder-back { left: 862px; top: 0; width: 338px; height: 532px; }
  .folder-back .brand { left: 0; width: 100%; top: 32px; font-size: 14px; }
  .folder-back .rule.light { left: 0; top: 470px; width: 100%; height: 2px; }

  /* envelopes */
  .envelope-front { left: 248px; top: 561px; width: 463px; height: 205px; }
  .envelope-front .brand { left: 22px; top: 28px; font-size: 12px; }
  .envelope-front .rule { left: 0; top: 172px; width: 100%; height: 5px; }

  .envelope-back { left: 737px; top: 561px; width: 463px; height: 206px; }
  .envelope-back .flap { position: absolute; left: 0; top: 0; }
  .envelope-back .brand { left: 0; width: 100%; top: 118px; font-size: 12px; }
  .envelope-back .rule { left: 0; top: 172px; width: 100%; height: 5px; }

  /* business cards */
  .card-front { left: 14px; top: 723px; width: 226px; height: 119px; }
  .card-front .brand { left: 24px; top: 32px; font-size: 10px; }
  .card-front .divider { left: 107px; top: 25px; height: 40px; }
  .card-front .rule { left: 11px; top: 89px; width: 205px; height: 4px; }

  .card-back { left: 16px; top: 880px; width: 224px; height: 118px; }
  .card-back .brand { left: 0; width: 100%; top: 42px; font-size: 13px; }

  /* mobile screen */
  .mobile-screen { left: 458px; top: 808px; width: 95px; height: 177px; }
  .mobile-screen .brand { left: 0; width: 100%; top: 76px; font-size: 9px; }

  /* compliment slip */
  .comp-slip { left: 660px; top: 822px; width: 486px; height: 155px; }
  .comp-slip .brand { left: 14px; top: 42px; font-size: 10px; }
  .comp-slip .divider { left: 92px; top: 31px; height: 47px; }
  .comp-slip .rule { left: 0; top: 89px; width: 100%; height: 4px; }
</style>
</head>
<body>

  <section class="item paper folder-front" aria-label="Presentation folder, front">
    <p class="brand">Blue Harbour<br>Marketing</p>
    <span class="divider"></span>
    <span class="rule"></span>
    <span class="band"></span>
  </section>

  <div class="pencil" style="left:123px" aria-label="Branded pencil">
    <svg class="tip" width="14" height="16" viewBox="0 0 14 16"><polygon points="7,0 14,16 0,16" fill="#e2c49b"/><polygon points="7,0 9,5 5,5" fill="#222"/></svg>
    <span class="body"></span>
  </div>
  <div class="pencil" style="left:150px" aria-label="Branded pencil">
    <svg class="tip" width="14" height="16" viewBox="0 0 14 16"><polygon points="7,0 14,16 0,16" fill="#e2c49b"/><polygon points="7,0 9,5 5,5" fill="#222"/></svg>
    <span class="body"></span>
  </div>
  <div class="pencil" style="left:177px" aria-label="Branded pencil">
    <svg class="tip" width="14" height="16" viewBox="0 0 14 16"><polygon points="7,0 14,16 0,16" fill="#e2c49b"/><polygon points="7,0 9,5 5,5" fill="#222"/></svg>
    <span class="body"></span>
  </div>

  <section class="item paper letterhead" aria-label="Letterhead">
    <p class="brand centered">Blue Harbour<br>Marketing</p>
    <p class="watermark" aria-hidden="true">Blue<br>Harbour<br>Marketing</p>
    <span class="rule"></span>
  </section>

  <section class="item red folder-back" aria-label="Presentation folder, back">
    <p class="brand on-red">Blue Harbour<br>Marketing</p>
    <span class="rule light"></span>
  </section>

  <section class="item paper envelope-front" aria-label="Envelope, front">
    <p class="brand">Blue Harbour<br>Marketing</p>
    <span class="rule"></span>
  </section>

  <section class="item paper envelope-back" aria-label="Envelope, back">
    <svg class="flap" width="463" height="48" viewBox="0 0 463 48">
      <path d="M0 0 H463 V44 Q463 38 440 36 H24 Q0 38 0 44 Z" fill="var(--brand-red)"/>
    </svg>
    <p class="brand centered">Blue Harbour<br>Marketing</p>
    <span class="rule"></span>
  </section>

  <section class="item paper card-front" aria-label="Business card, front">
    <p class="brand">Blue Harbour<br>Marketing</p>
    <span class="divider"></span>
    <span class="rule"></span>
  </section>

  <section class="item red card-back" aria-label="Business card, back">
    <p class="brand on-red">Blue Harbour<br>Marketing</p>
  </section>

  <section class="item red mobile-screen" aria-label="Mobile splash screen">
    <p class="brand on-red">Blue Harbour<br>Marketing</p>
  </section>

  <section class="item paper comp-slip" aria-label="Compliment slip">
    <p class="brand">Blue Harbour<br>Marketing</p>
    <span class="divider"></span>
    <span class="rule"></span>
  </section>

</body>
</html>
```